A label for a massage gel with bee venom for chronic pain

The product is a massage gel with natural ingredients that contain beehive products (propolis, bee venom, bee wax) and has an effect similar to Tor Vell.

The product is packed in a 250 ml plastic jar, and we need a proper label.

```html
<!DOCTYPE html>
<html lang="en">
<head>
<meta charset="UTF-8">
<title>Massage Gel Label</title>
<link href="https://fonts.googleapis.com/css2?family=Oswald:wght@400;500;600&family=Roboto:ital,wght@1,700;1,900&display=swap" rel="stylesheet">
<style>
  :root {
    --page-bg: #ffffff;
    --red-deep: #c4141f;
    --red-mid: #d92620;
    --orange-glow: #e8431c;
    --white: #ffffff;
    --ink: #111111;
    --figure-tint: rgba(255, 190, 160, 0.26);
  }
  * { margin: 0; padding: 0; box-sizing: border-box; }
  html, body {
    width: 1200px; height: 770px; overflow: hidden;
    background: var(--page-bg);
  }
  .label {
    position: absolute;
    left: 40px; top: 148px;
    width: 1120px; height: 473px;
    background: linear-gradient(90deg, var(--red-deep) 0%, var(--red-mid) 30%, var(--orange-glow) 55%, var(--red-mid) 78%, var(--red-deep) 100%);
    box-shadow: 0 6px 14px rgba(0,0,0,0.25);
    overflow: hidden;
    color: var(--white);
    font-family: 'Oswald', sans-serif;
  }
  .figure-area {
    position: absolute;
    left: 616px; top: 14px;
    width: 222px; height: 459px;
    border-radius: 90px 90px 10px 10px;
    background: linear-gradient(180deg, var(--figure-tint), rgba(255,190,160,0.16));
  }
  .brand {
    position: absolute; left: 477px; top: 34px; width: 160px;
    text-align: center;
    font-family: 'Oswald', sans-serif; font-weight: 500;
    font-size: 24px; line-height: 32px; letter-spacing: 3px;
    white-space: nowrap;
  }
  .tagline {
    position: absolute; left: 387px; top: 96px; width: 340px;
    text-align: center;
    font-family: 'Roboto', sans-serif; font-style: italic; font-weight: 900;
    font-size: 30px; line-height: 36px;
    white-space: nowrap;
  }
  .claim-band {
    position: absolute; left: 410px; top: 133px; width: 282px; height: 33px;
    background: linear-gradient(90deg, rgba(255,255,255,0) 0%, #ffffff 22%, #ffffff 78%, rgba(255,255,255,0) 100%);
    color: var(--ink);
    text-align: center;
    font-family: 'Oswald', sans-serif; font-weight: 500;
    font-size: 22px; line-height: 33px;
    white-space: nowrap;
  }
  .product-name {
    position: absolute; left: 557px; top: 162px;
    transform: translateX(-50%);
    white-space: nowrap;
    font-family: 'Oswald', sans-serif; font-weight: 600;
    font-size: 88px; line-height: 96px;
    letter-spacing: -2px;
  }
  .relief-list {
    position: absolute; left: 434px; top: 260px;
    list-style: none;
    font-family: 'Roboto', sans-serif; font-style: italic; font-weight: 700;
    font-size: 25px; line-height: 28px;
    white-space: nowrap;
  }
  .relief-list::before {
    content: ""; position: absolute; left: 5px; top: 14px; width: 3px; height: 84px;
    background: var(--white);
  }
  .relief-list li { position: relative; padding-left: 22px; }
  .relief-list li::before {
    content: ""; position: absolute; left: 0; top: 9px; width: 12px; height: 12px;
    border-radius: 50%; background: var(--white);
  }
  .ingredients {
    position: absolute; left: 361px; top: 394px;
    display: flex; align-items: center; gap: 8px;
    font-size: 21px; font-weight: 500; line-height: 30px;
    white-space: nowrap;
  }
  .leaf-icon { width: 30px; height: 30px; margin-right: -6px; }
  .with-badge {
    background: var(--white); color: var(--red-deep);
    font-family: 'Roboto', sans-serif; font-style: italic; font-weight: 900;
    font-size: 16px; line-height: 20px; padding: 1px 6px;
  }
  .net-weight {
    position: absolute; left: 460px; top: 432px; width: 230px;
    text-align: center; font-size: 19px; font-weight: 400; line-height: 28px;
    white-space: nowrap;
  }
</style>
</head>
<body>
  <div class="label">
    <div class="figure-area" role="img" aria-label="Faint human body silhouette with glowing pain points"></div>

    <div class="brand">HIVEWELL</div>

    <div class="tagline">With Bee Venom</div>
    <div class="claim-band">FOR CHRONIC PAIN.</div>
    <h1 class="product-name">MASSAGE GEL</h1>

    <ul class="relief-list">
      <li>Backache</li>
      <li>Stiff Neck</li>
      <li>Joint Pain</li>
      <li>Sore Muscle</li>
    </ul>

    <div class="ingredients">
      <svg class="leaf-icon" viewBox="0 0 30 30" aria-hidden="true">
        <path d="M4 26 C4 12 12 4 26 4 C26 18 18 26 4 26 Z" fill="#ffffff"/>
        <path d="M6 24 C12 16 16 12 22 8" stroke="#d92620" stroke-width="2" fill="none"/>
      </svg>
      <span class="with-badge">WITH:</span>
      <span class="ingredient-text">PROPOLIS, BEE VENOM &amp; BEE WAX.</span>
    </div>

    <div class="net-weight">NET WT 3 OZ (85 g)</div>
  </div>
</body>
</html>
```